Crestline Lending Group Business Cards

We are looking to revamp the current business cards each of our locations uses. We are a lending company that specializes in personal loans, title loans, and tax services. We have locations in New Mexico, Texas, and Oklahoma.

We would like a cleaner, sleeker look while still highlighting what we offer. Title Loans, Personal Loans & Tax Services. We also want to include our referral fee somewhere on the card. We would like to see an English option as well as a Spanish option for the cards.

PLEASE NOTE: Some business cards do not include the employee's name but just the store's location, while others will include both.

These are double-sided business cards, and we would like to see proof if possible. I have included proofs of our current business cards for you to review below, as well as our company logo. Feel free to get creative with the logo, etc! Colors should match the logo; however, you do not need to use all of our logo colors if you don't want to.

```html
<!DOCTYPE html>
<html lang="en">
<head>
<meta charset="utf-8">
<title>Crestline Lending Group – Business Cards</title>
<link rel="stylesheet" href="https://fonts.googleapis.com/css2?family=Poppins:wght@300;400;600;700&family=Archivo:wght@400;600;800&display=swap">
<style>
  :root {
    --green: #0b6b2e;
    --green-deep: #085424;
    --red: #d9161f;
    --white: #ffffff;
    --paper: #f6f6f4;
    --ink: #2b2b2b;
    --backdrop: #e4e2dd;
  }
  * { box-sizing: border-box; margin: 0; padding: 0; }
  html, body { width: 1200px; height: 900px; overflow: hidden; }
  body {
    background: var(--backdrop);
    font-family: "Poppins", sans-serif;
    position: relative;
  }
  .card {
    position: absolute;
    top: 100px;
    width: 400px;
    height: 700px;
    border-radius: 6px;
    overflow: hidden;
    box-shadow: 0 10px 30px rgba(0,0,0,.18);
  }
  .card--front { left: 150px; background: var(--green); }
  .card--back { left: 650px; background: var(--white); }

  /* front */
  .card__shapes { position: absolute; inset: 0; }
  .services {
    position: absolute; left: 28px; top: 36px; width: 344px; height: 210px;
    background: var(--white); border-radius: 18px;
    padding: 46px 0 0 40px; list-style: none;
  }
  .services__item {
    display: flex; align-items: center; gap: 12px;
    color: var(--red); font-weight: 600; font-size: 21px; line-height: 1; margin-bottom: 16px;
  }
  .tick {
    width: 22px; height: 22px; border-radius: 6px; background: var(--red);
    display: inline-flex; align-items: center; justify-content: center; flex: none;
  }
  .website {
    position: absolute; left: 44px; top: 330px;
    display: flex; align-items: center; gap: 10px;
    color: var(--white); font-size: 15px; font-weight: 400;
  }
  .brand {
    position: absolute; left: 0; right: 0; top: 470px; text-align: center;
  }
  .brand__name {
    color: var(--green); font-weight: 700; font-size: 56px; line-height: 1; letter-spacing: -.5px;
  }
  .brand__tagline {
    margin-top: 14px; color: var(--red); font-size: 15px; letter-spacing: 5px; font-weight: 400;
  }

  /* back */
  .person { position: absolute; left: 40px; top: 70px; font-family: "Archivo", sans-serif; }
  .person__name { color: var(--red); font-weight: 800; font-size: 30px; letter-spacing: .5px; }
  .person__role { color: var(--green); font-weight: 400; font-size: 15px; margin-top: 2px; letter-spacing: .5px; }
  .contacts { list-style: none; margin-top: 40px; }
  .contacts__item {
    display: flex; align-items: center; gap: 12px; font-size: 13px; color: var(--ink); margin-bottom: 14px;
  }
  .contacts__icon {
    width: 26px; height: 26px; border-radius: 50%; background: var(--red);
    display: inline-flex; align-items: center; justify-content: center; flex: none;
  }
  .back-brand {
    position: absolute; right: 40px; top: 330px;
    color: var(--green); font-weight: 700; font-size: 34px; font-family: "Poppins", sans-serif;
  }
  .referral {
    position: absolute; left: 0; right: 0; top: 500px; text-align: center; color: var(--white);
  }
  .referral__lead { font-weight: 300; font-size: 22px; letter-spacing: 1px; }
  .referral__offer { display: flex; align-items: center; justify-content: center; gap: 12px; margin-top: 14px; }
  .referral__get { font-family: "Archivo", sans-serif; font-weight: 800; font-size: 34px; }
  .referral__pill {
    background: var(--white); color: var(--green); font-family: "Archivo", sans-serif;
    font-weight: 800; font-size: 20px; padding: 6px 12px; border-radius: 8px;
  }
  .referral__amount {
    font-family: "Archivo", sans-serif; font-weight: 800; font-size: 64px; line-height: 1;
    color: transparent; -webkit-text-stroke: 2px var(--white);
  }
</style>
</head>
<body>

<section class="card card--front" aria-label="Card front">
  <svg class="card__shapes" width="400" height="700" viewBox="0 0 400 700">
    <path d="M28 300 Q28 276 52 276 L400 276 L400 700 L28 700 Z" fill="var(--red)"/>
    <path d="M0 420 L200 420 Q240 420 250 385 Q258 360 290 360 L400 360 L400 700 L0 700 Z" fill="var(--paper)"/>
  </svg>

  <ul class="services">
    <li class="services__item"><span class="tick"><svg width="12" height="12" viewBox="0 0 12 12"><path d="M2 6.5 L5 9 L10 3" stroke="#fff" stroke-width="2" fill="none" stroke-linecap="round"/></svg></span>Title Loans</li>
    <li class="services__item"><span class="tick"><svg width="12" height="12" viewBox="0 0 12 12"><path d="M2 6.5 L5 9 L10 3" stroke="#fff" stroke-width="2" fill="none" stroke-linecap="round"/></svg></span>Personal Loans</li>
    <li class="services__item"><span class="tick"><svg width="12" height="12" viewBox="0 0 12 12"><path d="M2 6.5 L5 9 L10 3" stroke="#fff" stroke-width="2" fill="none" stroke-linecap="round"/></svg></span>Tax Services</li>
  </ul>

  <p class="website">
    <svg width="16" height="16" viewBox="0 0 16 16"><circle cx="8" cy="8" r="7" fill="#fff"/><path d="M1 8 H15 M8 1 C4 5 4 11 8 15 M8 1 C12 5 12 11 8 15" stroke="var(--red)" stroke-width="1.2" fill="none"/></svg>
    www.crestlinelending.com
  </p>

  <div class="brand">
    <p class="brand__name">Crestline</p>
    <p class="brand__tagline">LOANS – PRESTAMOS</p>
  </div>
</section>

<section class="card card--back" aria-label="Card back">
  <svg class="card__shapes" width="400" height="700" viewBox="0 0 400 700">
    <path d="M0 440 Q0 420 20 420 L130 420 Q150 420 155 440 Q170 480 210 480 Q250 480 262 440 Q268 420 290 420 L380 420 Q400 420 400 440 L400 700 L0 700 Z" fill="var(--green)"/>
  </svg>

  <div class="person">
    <h1 class="person__name">DANIEL WHITFORD</h1>
    <p class="person__role">BRANCH MANAGER</p>
    <ul class="contacts">
      <li class="contacts__item"><span class="contacts__icon"><svg width="12" height="12" viewBox="0 0 12 12"><path d="M3 1 L5 3.5 L4 5 Q5 7 7 8 L8.5 7 L11 9 L10 11 Q4 11 1 2 Z" fill="#fff"/></svg></span>(02) 5550 1842</li>
      <li class="contacts__item"><span class="contacts__icon"><svg width="12" height="12" viewBox="0 0 12 12"><rect x="1" y="2.5" width="10" height="7" rx="1" fill="#fff"/><path d="M1.5 3 L6 6.5 L10.5 3" stroke="var(--red)" stroke-width="1" fill="none"/></svg></span>d.whitford@crestlinelending.com</li>
      <li class="contacts__item"><span class="contacts__icon"><svg width="12" height="12" viewBox="0 0 12 12"><path d="M6 11 C3 7 2.5 5.5 2.5 4.5 A3.5 3.5 0 0 1 9.5 4.5 C9.5 5.5 9 7 6 11 Z" fill="#fff"/><circle cx="6" cy="4.5" r="1.3" fill="var(--red)"/></svg></span>218 Harlow Court, Tulsa, Oklahoma</li>
    </ul>
  </div>

  <p class="back-brand">Crestline</p>

  <div class="referral">
    <p class="referral__lead">Refer a friend</p>
    <div class="referral__offer">
      <span class="referral__get">GET</span>
      <span class="referral__pill">UP TO</span>
    </div>
    <p class="referral__amount">$100</p>
  </div>
</section>

</body>
</html>
```